TONVALE - A modern gin bottle label

Design of a bottle label in a modern fresh design. The name of the gin is "TONVALE Phantom Batch K7". Please take a look at the tonvale.de website. on the main page of tonvale.de you can breathe the design direction here: 1) the taste of the gin should be composed of 10 botanicals ... an important scent note. ) a distinctive flavor is spicy and fresh 3.) The filling volume is 0.5 liters 4.) the alcohol content is 43% vol. 5.) the variety is called "dry gin" 6.) tonvale stands for "energy" and "love"

Target Market(s)

Alcohol consumer

Colors

Designer to choose colors to be used in the design.

Requirements
Must have
• the tonvale corporate logo must be included, the name of the gin is "TONVALE Phantom Batch K7"
Nice to have
• Please use the bottles template in the appendix. (The Black Bottles) they can use the saying "DESTILLED & BOTTLED BY OLD MARINER" in small letters

```html
<!DOCTYPE html>
<html lang="en">
<head>
<meta charset="utf-8">
<title>TONVALE Phantom Batch K7 – Dry Gin Label</title>
<link rel="stylesheet" href="https://fonts.googleapis.com/css2?family=Anton&family=Montserrat:wght@700&family=Oswald:wght@200;300&family=Quicksand:wght@500&display=swap">
<style>
  :root {
    --page: #ffffff;
    --label-top: #0d0b10;
    --label-mid: #2a2530;
    --label-haze: #4a4352;
    --label-bottom: #141117;
    --moon-core: rgba(150, 90, 20, 0.55);
    --moon-edge: rgba(80, 50, 20, 0);
    --accent-orange: #ff7a1a;
    --acid-green: #a8d420;
    --text-light: #e8e6ea;
    --text-muted: #b9b4bd;
  }
  * { box-sizing: border-box; margin: 0; padding: 0; }
  html, body {
    width: 1200px; height: 1200px; overflow: hidden;
    background: var(--page);
  }
  .canvas {
    width: 1200px; height: 1200px;
    display: flex; align-items: center; justify-content: center;
  }
  .label {
    position: relative;
    width: 740px; height: 1086px;
    overflow: hidden;
    background: linear-gradient(180deg, var(--label-top) 0%, var(--label-top) 30%, var(--label-mid) 55%, var(--label-haze) 72%, var(--label-bottom) 100%);
  }
  .moon {
    position: absolute; left: 224px; top: 48px;
    width: 308px; height: 308px; border-radius: 50%;
    background: radial-gradient(circle, var(--moon-core) 0%, rgba(110, 70, 20, 0.4) 55%, var(--moon-edge) 72%);
  }
  .brand {
    position: absolute; left: 0; right: 0; top: 150px;
    display: flex; flex-direction: column; align-items: center; gap: 14px;
  }
  .brand-dot {
    width: 26px; height: 26px; border-radius: 50%;
    background: var(--accent-orange);
  }
  .brand-name {
    font-family: "Montserrat", sans-serif; font-weight: 700;
    font-size: 44px; letter-spacing: 6px;
    color: var(--text-light);
  }
  .graveyard-scene {
    position: absolute; left: 0; right: 0; top: 413px; height: 365px;
    background: linear-gradient(180deg, rgba(20, 18, 24, 0) 0%, rgba(30, 28, 34, 0.6) 45%, rgba(18, 17, 20, 0.9) 85%, rgba(60, 55, 68, 0.5) 100%);
  }
  .title {
    position: absolute; left: 0; right: 0; top: 555px;
    text-align: center;
    font-family: "Anton", sans-serif;
    font-size: 168px; line-height: 1; letter-spacing: 4px;
    color: var(--acid-green);
  }
  .batch {
    position: absolute; left: 0; right: 0; top: 795px;
    text-align: center;
    font-family: "Oswald", sans-serif; font-weight: 200;
    font-size: 52px; letter-spacing: 14px;
    color: var(--text-light);
  }
  .variety {
    position: absolute; left: 0; right: 0; top: 905px;
    text-align: center;
    font-family: "Quicksand", sans-serif; font-weight: 500;
    font-size: 60px; letter-spacing: 5px;
    color: var(--acid-green);
  }
  .maker {
    position: absolute; left: 0; right: 0; top: 980px;
    text-align: center;
    font-family: "Oswald", sans-serif; font-weight: 300;
    font-size: 22px; letter-spacing: 1px;
    color: var(--text-muted);
  }
  .spec {
    position: absolute; top: 1020px;
    font-family: "Oswald", sans-serif; font-weight: 300;
    font-size: 34px; letter-spacing: 1px;
    color: var(--text-muted);
  }
  .spec-abv { left: 38px; }
  .spec-volume { right: 30px; }
</style>
</head>
<body>
  <main class="canvas">
    <section class="label">
      <div class="moon"></div>
      <header class="brand">
        <span class="brand-dot"></span>
        <span class="brand-name">TONVALE</span>
      </header>
      <div class="graveyard-scene" role="img" aria-label="Night graveyard with crosses, tombstones and flying bats in dark silhouettes"></div>
      <h1 class="title">PHANTOM</h1>
      <p class="batch">BATCH K7</p>
      <p class="variety">DRY GIN</p>
      <p class="maker">DESTILLED &amp; BOTTLED BY OLD MARINER</p>
      <span class="spec spec-abv">43% VOL</span>
      <span class="spec spec-volume">0.5 L</span>
    </section>
  </main>
</body>
</html>
```